Regenerative Medicine Brochure

I want a clean modern bi-fold or tri-fold brochure. We offer non-surgical joint repair for knees, shoulders, and hips. We have many services available including regenerative medicine including stem cell allograft, palatelet rich plasma, prolotherapy, triggerpoint injection, chiropractic and rehab therapies. We are a modern multidisciplinary clinic in coastal California. My logo is already complete and is a vibrant green color. I prefer lots of white space with some areas for service description and what conditions may benefit from the services. Design should convey modern treatments, upscale office and practice, and our target audience is older adults who want to maintain an active pain-free lifestyle.

Target Market(s)

Sports injuries, athletes, seniors who are active, knee pain, shoulder pain, arthritis.

Industry/Entity Type

Alternative Medicine

Font styles to use
Serif

Colors
9bcb3c

Requirements
Must have
• Small white space where we can write date, time, location of next event/class. Colors in brochure to coordinate with logo colors provided.

```html
<!DOCTYPE html>
<html lang="en">
<head>
<meta charset="utf-8">
<title>Tidewell Spine &amp; Joint – Trifold Brochure</title>
<link href="https://fonts.googleapis.com/css2?family=Montserrat:wght@400;600;700;800&family=Raleway:wght@400;500;600&display=swap" rel="stylesheet">
<style>
  :root{
    --page-bg:#b9b9b9;
    --green:#3a8a2e;
    --green-bright:#45a035;
    --ink:#222;
    --text:#3a3a3a;
    --paper:#ffffff;
    --paper-gray:#eceef0;
    --white:#ffffff;
  }
  *{box-sizing:border-box;margin:0;padding:0}
  html,body{width:1200px;height:2400px;overflow:hidden}
  body{background:var(--page-bg);font-family:"Raleway",sans-serif;color:var(--text);position:relative}
  .brochure{position:absolute;left:50px;top:811px;width:1100px;height:778px;display:grid;grid-template-columns:repeat(3,1fr);box-shadow:0 8px 24px rgba(0,0,0,.25)}
  .panel{position:relative;height:100%;overflow:hidden}

  /* Left panel */
  .panel--qa{background:var(--paper)}
  .photo--pain{position:absolute;left:0;top:0;width:100%;height:316px;background:linear-gradient(160deg,#e9eaec 0%,#b9aea3 35%,#7a6656 60%,#cfc8c0 100%)}
  .qa-title{position:absolute;left:19px;top:334px;font-family:"Montserrat",sans-serif;font-weight:800;font-size:16.5px;color:var(--ink);letter-spacing:.3px}
  .qa-bar{position:absolute;left:0;top:379px;width:100%;height:20px}
  .qa-bar__label{position:absolute;left:0;top:0;height:20px;background:var(--green);color:var(--white);font-family:"Montserrat",sans-serif;font-weight:500;font-size:12px;line-height:20px;padding:0 18px 0 19px}
  .qa-bar__rule{position:absolute;left:0;right:0;top:18px;height:2px;background:var(--green)}
  .qa-body{position:absolute;left:19px;right:16px;top:410px;font-size:7.6px;line-height:1.5;text-align:justify}
  .qa-body p{margin-bottom:5px}
  .qa-sub{font-family:"Montserrat",sans-serif;font-size:10px;color:var(--ink);margin:8px 0 12px!important;text-align:left}
  .areas{display:grid;grid-template-columns:1fr 1fr .75fr;row-gap:4px;font-size:8px;margin-bottom:12px;text-transform:uppercase}
  .areas li{list-style:none}
  .areas li::before{content:"\2713";color:var(--green);margin-right:3px}
  .panel-url{position:absolute;left:0;right:0;bottom:14px;text-align:center;font-size:13.5px;font-weight:500}
  .panel--qa .panel-url{color:var(--ink)}

  /* Middle panel */
  .panel--contact{background:var(--green);color:var(--white)}
  .section-head{position:absolute;left:28px;right:28px;display:flex;align-items:center;gap:12px;font-family:"Montserrat",sans-serif;font-weight:700;font-size:15px;letter-spacing:.5px}
  .section-head::before,.section-head::after{content:"";flex:1;height:1.5px;background:var(--white)}
  .section-head--hours{top:136px}
  .section-head--touch{top:376px;left:46px;right:46px}
  .hours{position:absolute;left:49px;top:170px;width:260px;font-size:11.5px;line-height:20.5px}
  .hours div{display:flex}
  .hours dt{width:145px}
  .contact-list{position:absolute;left:0;right:0;top:412px;text-align:center;list-style:none;font-size:16px;letter-spacing:.3px}
  .contact-list li{display:flex;flex-direction:column;align-items:center}
  .contact-list svg{width:15px;height:15px;margin-bottom:6px}
  .contact-list .c-phone{margin-bottom:30px}
  .contact-list .c-address{margin-bottom:28px;line-height:1.3}
  .contact-list .c-mail{margin-bottom:26px}
  .panel--contact .panel-url{font-size:14px}

  /* Right panel */
  .panel--cover{background:linear-gradient(180deg,var(--paper-gray),#f6f6f7 40%)}
  .brand{position:absolute;left:27px;top:72px;display:flex;align-items:center;gap:10px;font-family:"Montserrat",sans-serif;font-weight:600;font-size:24px;color:var(--ink)}
  .brand__mark{width:12px;height:12px;background:var(--green-bright)}
  .cover-title{position:absolute;left:27px;top:175px;font-family:"Montserrat",sans-serif;font-size:17.5px;line-height:1.4;color:var(--ink);font-weight:800}
  .cover-title .lead{color:var(--green-bright);font-weight:400}
  .cover-title .accent{color:var(--green-bright)}
  .cover-title .amp{font-weight:400}
  .cover-intro{position:absolute;left:27px;right:16px;top:233px;font-size:7.8px;line-height:1.55;text-align:justify;color:var(--text)}
  .photo--beach{position:absolute;left:0;right:0;top:300px;bottom:0;background:linear-gradient(180deg,#f1f0ec 0%,#dcd6c8 35%,#d9b777 65%,#cf9a45 100%)}
  .panel--cover .panel-url{color:var(--ink);font-size:13.5px}
</style>
</head>
<body>
<main class="brochure">

  <section class="panel panel--qa">
    <div class="photo photo--pain" role="img" aria-label="Photo of a woman holding her neck in pain, seated on a sofa"></div>
    <h2 class="qa-title">REGENERATIVE MEDICINE Q &amp; A</h2>
    <div class="qa-bar"><span class="qa-bar__rule"></span><span class="qa-bar__label">What Is Regenerative Medicine?</span></div>
    <div class="qa-body">
      <p>Regenerative medicine is a form of biotechnology that involves injecting regenerative medicine products into injured tissues to help your body repair damage. Regenerative medicine uses tissue engineering techniques to repair muscles, ligaments, cartilage, and tendons damaged by injuries, overuse, and osteoarthritis. The medical providers at Tidewell Spine &amp; Joint select from a variety of available treatments and products. These include amniotic allografts, hyaluronic acid, regenerative cells, and cytokines which are powerful growth factors that may help regenerate your own body's tissues.</p>
      <p>After you're injection with the amniotic allograft serum, the growth factors trigger repair at the site of injection. Over the course of the next several weeks, cells grow and multiply forming new tissue.</p>
      <p class="qa-sub">Regenerative Medicine May Be Used In The Following Areas:</p>
      <ul class="areas">
        <li>Shoulder</li><li>Elbow</li><li>Wrist</li>
        <li>Hip</li><li>Ankle</li><li>Knee</li>
      </ul>
      <p>There are many additional types of bone and soft tissue problems, including arthritis, that these injections may benefit.</p>
      <p>With regenerative medicine and amniotic allograft treatments, the team supports the natural healing abilities of your body without the need for drugs or surgical repair and painful recovery. However, not all forms of regenerative medicine are equal. At Tidewell Spine &amp; Joint, the team only works with the best regenerative medicine labs to ensure that the right kind of products are selected and that they are of the best quality and highest safety.</p>
    </div>
    <p class="panel-url">www.tidewellspineandjoint.com</p>
  </section>

  <section class="panel panel--contact">
    <h3 class="section-head section-head--hours">OPENING HOURS</h3>
    <dl class="hours">
      <div><dt>MONDAY-</dt><dd>8:00 am - 6:00 pm</dd></div>
      <div><dt>TUESDAY-</dt><dd>8:00 am - 12:00 pm</dd></div>
      <div><dt>WEDNESDAY-</dt><dd>8:00 am - 6:00 pm</dd></div>
      <div><dt>THURSDAY-</dt><dd>8:00 am - 12:00 pm</dd></div>
      <div><dt>FRIDAY-</dt><dd>8:00 am - 6:00 pm</dd></div>
      <div><dt>SATURDAY-</dt><dd>Closed</dd></div>
      <div><dt>SUNDAY-</dt><dd>Closed</dd></div>
    </dl>
    <h3 class="section-head section-head--touch">GET IN TOUCH</h3>
    <ul class="contact-list">
      <li class="c-phone">
        <svg viewBox="0 0 16 16"><circle cx="8" cy="8" r="8" fill="#fff"/><path d="M5.2 4.2l1.4-.3.8 1.9-.9.7c.5 1 1.2 1.7 2.1 2.1l.7-.9 1.9.8-.3 1.4c-3.2.2-5.9-2.5-5.7-5.7z" fill="#3a8a2e"/></svg>
        805-555-0142
      </li>
      <li class="c-phone">
        <svg viewBox="0 0 16 16"><circle cx="8" cy="8" r="8" fill="#fff"/><rect x="5.7" y="3.8" width="4.6" height="8.4" rx="0.8" fill="#3a8a2e"/><rect x="6.5" y="5" width="3" height="5" fill="#fff"/></svg>
        805-555-0178
      </li>
      <li class="c-address">
        <svg viewBox="0 0 16 16"><circle cx="8" cy="8" r="8" fill="#fff"/><path d="M8 3.5a3 3 0 0 0-3 3c0 2.2 3 5.8 3 5.8s3-3.6 3-5.8a3 3 0 0 0-3-3z" fill="#3a8a2e"/><circle cx="8" cy="6.5" r="1.1" fill="#fff"/></svg>
        240 Harbor Lane<br>Seabright, CA 93010
      </li>
      <li class="c-mail">
        <svg viewBox="0 0 16 16"><circle cx="8" cy="8" r="8" fill="#fff"/><rect x="4" y="5.2" width="8" height="5.6" fill="#3a8a2e"/><path d="M4 5.2l4 3 4-3" fill="none" stroke="#fff" stroke-width=".9"/></svg>
        info@tidewellspineandjoint.com
      </li>
      <li>
        <svg viewBox="0 0 16 16"><circle cx="8" cy="8" r="8" fill="#fff"/><circle cx="8" cy="8" r="4" fill="none" stroke="#3a8a2e" stroke-width="1"/><path d="M4 8h8M8 4c-1.6 2.2-1.6 5.8 0 8M8 4c1.6 2.2 1.6 5.8 0 8" fill="none" stroke="#3a8a2e" stroke-width=".8"/></svg>
      </li>
    </ul>
    <p class="panel-url">www.tidewellspineandjoint.com</p>
  </section>

  <section class="panel panel--cover">
    <div class="brand"><span class="brand__mark"></span><span>Tidewell Spine &amp; Joint</span></div>
    <h1 class="cover-title"><span class="lead">FOR </span><span class="accent">JOINT ARTHRITIS</span> <span class="lead">&amp;</span><br>MUSCLE PAIN <span class="amp">&amp;</span> INJURIES</h1>
    <p class="cover-intro">The team at Tidewell Spine &amp; Joint offers minimally invasive regenerative medicine techniques to help you recover from chronic pain. <strong>Located in Seabright, California</strong>, the medical team utilizes advanced restorative techniques to support the natural healing of injured joints and soft tissues without the need for surgery. To learn more, schedule a consultation online or by phone today.</p>
    <div class="photo photo--beach" role="img" aria-label="Photo of an older couple walking hand in hand along a sunlit beach"></div>
    <p class="panel-url">www.tidewellspineandjoint.com</p>
  </section>

</main>
</body>
</html>
```